Obrelo Business Card

Need a double sided business card. Would like the business card to have the logo on one side and the employees details and business contact details on the other.

Business

```html
<!DOCTYPE html>
<html lang="en">
<head>
<meta charset="utf-8">
<title>Obrelo Business Card</title>
<link href="https://fonts.googleapis.com/css2?family=Lato:wght@300;400;700;900&display=swap" rel="stylesheet">
<style>
  :root {
    --page-bg: #e9e6e1;
    --card-dark: #121212;
    --card-dark-edge: #2a2a2a;
    --card-light: #f6f6f6;
    --accent: #e5502f;
    --accent-deep: #d8431f;
    --ink: #222222;
    --ink-soft: #5a5a5a;
    --rule: #9a9a9a;
    --white: #ffffff;
  }
  * { margin: 0; padding: 0; box-sizing: border-box; }
  html, body {
    width: 1200px;
    height: 913px;
    overflow: hidden;
    background: var(--page-bg);
    font-family: "Lato", Arial, sans-serif;
  }
  .canvas {
    position: relative;
    width: 1200px;
    height: 913px;
  }
  .card {
    position: absolute;
    width: 560px;
    height: 320px;
    border-radius: 3px;
    overflow: hidden;
    box-shadow: 0 14px 30px rgba(0,0,0,0.22);
  }

  /* Front side */
  .card--front {
    left: 90px;
    top: 110px;
    background: linear-gradient(135deg, var(--card-dark-edge) 0%, var(--card-dark) 55%, #0a0a0a 100%);
  }
  .brand-band {
    position: absolute;
    left: 0;
    top: 178px;
    width: 330px;
    height: 44px;
    background: linear-gradient(90deg, var(--accent-deep), var(--accent));
    display: flex;
    align-items: center;
    justify-content: flex-end;
    padding-right: 18px;
  }
  .brand-name {
    color: var(--white);
    font-weight: 400;
    font-size: 25px;
    letter-spacing: 0.5px;
    text-transform: uppercase;
  }

  /* Back side */
  .card--back {
    left: 560px;
    top: 480px;
    background: var(--card-light);
  }
  .accent-square {
    position: absolute;
    left: 0;
    top: 200px;
    width: 74px;
    height: 62px;
    background: var(--accent);
  }
  .person {
    position: absolute;
    left: 94px;
    top: 176px;
  }
  .person-name {
    color: var(--accent);
    font-size: 27px;
    font-weight: 300;
    text-transform: uppercase;
    line-height: 1;
  }
  .person-name strong { font-weight: 900; }
  .person-role {
    margin-top: 4px;
    color: var(--ink);
    font-size: 17px;
    font-weight: 300;
    text-transform: uppercase;
    line-height: 1;
  }
  .person-role strong { font-weight: 900; }

  .contact {
    position: absolute;
    left: 330px;
    top: 40px;
    padding-left: 18px;
    border-left: 1px solid var(--rule);
    height: 104px;
  }
  .contact-list {
    list-style: none;
    color: var(--ink-soft);
    font-size: 11.5px;
    font-weight: 400;
    line-height: 19px;
  }
</style>
</head>
<body>
  <main class="canvas">
    <section class="card card--front" aria-label="Business card front">
      <div class="brand-band">
        <span class="brand-name">Inniti Obrelo</span>
      </div>
    </section>

    <section class="card card--back" aria-label="Business card back">
      <div class="contact">
        <ul class="contact-list">
          <li>+ 000 - 4821 - 3096</li>
          <li>admin@obrelo.com</li>
          <li>info@obrelostudio.com</li>
          <li>88 Harlow Street Avenue,</li>
          <li>Portland 54021</li>
        </ul>
      </div>
      <div class="accent-square"></div>
      <div class="person">
        <p class="person-name"><strong>Mara</strong> Velden</p>
        <p class="person-role"><strong>Art</strong> Director</p>
      </div>
    </section>
  </main>
</body>
</html>
```